Bref créative
Velvet Larder Business Cards
Logo has already been created!!
Bright & Fun-filled
Pete Hargrove
Owner
487 Cedar Ave.
Chicago, IL 60605
wxyz@mailbrook.net
www.myvelvetlarder.com
We were very very satisfied during our logo design contest. Lot of creative minds here and that brings me back again for our business cards! Here is a link to our prior project -
http://orders.brandcraftforge.com/contests/project-velvet-larder-pup
We are young and will be setting up in urban area. We would like this factor to reflect in our business cards. We found sample business cards that we like on web -
http://vorteksketch.net/inspirations/60-most-beautiful-and-creative-business-cards-design/
We are still deciding on color scheme so please feel free to use different pallet/scheme while altering business logo.
Should include a space for facebook and twitter icon and id as well. Use VLFacebook and VLTwitter as a dummy ids.
We are thinking that back of the business card would cover entire logo as a whole along with the website and/or tagline -
"There are local grocery stores and there is the Velvet Larder.
Experience the grocery shopping a Velvet Way!"

```html
<!DOCTYPE html>
<html lang="en">
<head>
<meta charset="utf-8">
<title>Velvet Larder – Business Card</title>
<link rel="stylesheet" href="https://fonts.googleapis.com/css2?family=Libre+Baskerville:wght@400;700&family=Montserrat:wght@400;600;700&display=swap">
<style>
  :root {
    --ink: #1d1b1a;
    --brand: #3a2a24;
    --rust: #8b2a1a;
    --grey: #8a8a8a;
    --grey-light: #a3a3a3;
    --paper: #ffffff;
    --texture-dark: #1f1915;
    --texture-mid: #4a3d34;
    --faint: rgba(210, 200, 190, 0.22);
    --url-light: #e8e2dc;
  }
  * { margin: 0; padding: 0; box-sizing: border-box; }
  html, body { width: 1200px; height: 686px; overflow: hidden; background: var(--paper); }
  .card { position: relative; width: 1200px; height: 686px; background: var(--paper); overflow: hidden; font-family: "Libre Baskerville", serif; }

  .card-back-panel {
    position: absolute; left: 0; top: 0; width: 600px; height: 686px;
    background: radial-gradient(ellipse at 40% 45%, var(--texture-mid) 0%, #332a24 45%, var(--texture-dark) 100%);
    overflow: hidden;
  }
  .panel-texture { position: absolute; inset: 0; }
  .panel-wordmark {
    position: absolute; font-family: "Montserrat", sans-serif; font-weight: 700;
    color: var(--faint); line-height: 1; letter-spacing: -4px; white-space: nowrap;
  }
  .panel-wordmark--top { top: 225px; left: -10px; font-size: 140px; }
  .panel-wordmark--bottom { top: 370px; left: 105px; font-size: 140px; }
  .panel-locale {
    position: absolute; left: -30px; top: 555px; font-family: "Montserrat", sans-serif; font-size: 30px;
    letter-spacing: 7px; color: var(--faint); transform: rotate(-6deg); transform-origin: left center; white-space: nowrap;
  }
  .panel-url {
    position: absolute; left: 562px; top: 343px; transform: translate(-50%, -50%) rotate(-90deg);
    font-family: "Montserrat", sans-serif; font-size: 27px; letter-spacing: 5px; color: var(--url-light);
    white-space: nowrap; text-transform: uppercase;
  }

  .brand { position: absolute; left: 600px; width: 600px; top: 100px; text-align: center; }
  .brand-name {
    font-family: "Montserrat", sans-serif; font-weight: 700; color: var(--brand);
    font-size: 64px; line-height: 0.95; letter-spacing: -1px;
  }
  .brand-locale {
    margin-top: 14px; font-family: "Montserrat", sans-serif; font-weight: 600; color: var(--rust);
    font-size: 19px; letter-spacing: 4px; text-transform: uppercase;
    border-top: 2px solid var(--rust); display: inline-block; padding-top: 6px;
  }

  .contact { position: absolute; left: 600px; width: 600px; top: 285px; text-align: center; }
  .contact-name { font-size: 60px; font-weight: 400; color: var(--ink); line-height: 1.1; }
  .contact-role { font-size: 40px; font-weight: 700; color: var(--grey); margin-top: 6px; }
  .contact-address { font-size: 34px; color: var(--grey-light); line-height: 1.5; margin-top: 6px; }

  .detail { position: absolute; display: flex; align-items: center; gap: 10px; color: var(--grey); font-family: "Libre Baskerville", serif; white-space: nowrap; }
  .detail--phone { left: 604px; top: 560px; font-size: 24px; }
  .detail--email { left: 900px; top: 560px; font-size: 21px; }
  .detail--community { left: 612px; top: 628px; font-size: 24px; }
  .detail--updates { left: 916px; top: 628px; font-size: 24px; }
  .detail-at { font-family: "Montserrat", sans-serif; font-size: 46px; color: var(--grey); line-height: 1; }
  .social-square { width: 42px; height: 42px; background: var(--grey-light); flex: none; }
</style>
</head>
<body>
  <main class="card">
    <section class="card-back-panel">
      <div class="panel-texture" role="img" aria-label="Dark grunge urban wall texture with pale streaks"></div>
      <div class="panel-wordmark panel-wordmark--top">velvet</div>
      <div class="panel-wordmark panel-wordmark--bottom">larder</div>
      <div class="panel-locale">SOUTH LOOP OF CHICAGO</div>
      <div class="panel-url">www.myvelvetlarder.com</div>
    </section>

    <header class="brand">
      <div class="brand-name">velvet<br>larder</div>
      <div class="brand-locale">South Loop of Chicago</div>
    </header>

    <section class="contact">
      <h1 class="contact-name">Pete Hargrove</h1>
      <p class="contact-role">owner</p>
      <p class="contact-address">487 Cedar Ave.<br>Chicago, Illinois</p>
    </section>

    <div class="detail detail--phone">
      <svg width="52" height="52" viewBox="0 0 52 52" aria-hidden="true">
        <circle cx="26" cy="26" r="23" fill="none" stroke="#8a8a8a" stroke-width="3"/>
        <path d="M17 15c2-2 4-2 5 0l3 5c1 2 0 3-1 4l-2 1c1 3 4 6 7 7l1-2c1-1 2-2 4-1l5 3c2 1 2 3 0 5-3 3-7 3-11 0-4-2-8-6-10-10-3-5-3-9-1-12z" fill="#8a8a8a"/>
      </svg>
      <span>+1 555.013.2468</span>
    </div>
    <div class="detail detail--email">
      <span class="detail-at">@</span>
      <span>wxyz@mailbrook.net</span>
    </div>
    <div class="detail detail--community">
      <span class="social-square"></span>
      <span>vlcommunity</span>
    </div>
    <div class="detail detail--updates">
      <span class="social-square"></span>
      <span>vlupdates</span>
    </div>
  </main>
</body>
</html>
```